KRV Holdfast Manufacturer New Web Design

We need a new theme designed for metal fastener manufacturing company, KRV Holdfast Group, a $60M division of Benmore Forge Holdings, Inc. We manufacture screw, pins and washers to industrial customers (non-Automotive) such as Tallow Appliance, Marcus Fenwold, BRU, Veltrin, etc. Our current website is www.holdfastparts.example. We would like to stick with the same logo/color scheme, however, I'm aiming to modernize the website's look and feel.

Here are some of our competitor's websites:
- https://www.torvanix.example/
- http://quellbrook.example/
- http://www.morrowbuiltcouplingworks.example/
- http://pegsandoddments.example/
- http://www.dunmerebolting.example/

Target Market(s)

We primarily want to target engineers working in the following markets:
- Appliance (Tallow Appliance, Kelvanor)
- Ag (Fenwold, BRU)
- Recreational Vehicle (Veltrin, Briar Fox)
- Outdoor Power (Oldmeadow, Vexa)

We secondarily want to target buyers working at the above markets as well as buyers at Fastener distributors such as Boltrin, Provision Dynamics, Hollis Parfet.

Industry/Entity Type

Metal Forging

Number of Pages Required

1 page

Requirements
Must have
• For products: "Threaded" product as the primary focus. "Pins" product is the secondary focus, followed by all others.
• Please use same logo and color scheme as I do not plan to change.
Nice to have
• Highlight our featured proprietary products (pamphlets attached). KRV Holdfast's KIN-V, LumDrive, Holdfast Spiral, Pelmont.

```html
<!DOCTYPE html>
<html lang="en">
<head>
<meta charset="utf-8">
<title>KRV Holdfast Group</title>
<link rel="stylesheet" href="https://fonts.googleapis.com/css2?family=Roboto:wght@300;400;500;700;900&display=swap">
<style>
  :root {
    --cyan: #00b4e0;
    --navy: #0b2638;
    --navy-deep: #0a2233;
    --teal: #12c9a9;
    --panel: #e5e8eb;
    --body-text: #4f5b66;
    --white: #ffffff;
    --steel-a: #2a5478;
    --steel-b: #173a5a;
  }
  * { margin: 0; padding: 0; box-sizing: border-box; }
  html, body { width: 1200px; height: 1200px; overflow: hidden; background: var(--white); font-family: 'Roboto', sans-serif; }
  .page { position: relative; width: 1200px; height: 1200px; overflow: hidden; }

  .main-nav { height: 40px; background: var(--cyan); display: flex; align-items: center; justify-content: space-between; padding: 0 136px 0 135px; }
  .main-nav a { color: var(--white); text-decoration: none; font-size: 12px; font-weight: 700; letter-spacing: 0.1px; }
  .main-nav a.is-active { color: var(--navy); }

  .site-header { height: 136px; background: var(--navy-deep); display: flex; align-items: center; justify-content: space-between; padding: 0 138px 0 136px; }
  .brand { display: flex; align-items: center; gap: 12px; }
  .brand-mark { width: 52px; height: 52px; border-radius: 50%; background: var(--cyan); }
  .brand-name { color: var(--cyan); font-size: 28px; font-weight: 400; }
  .tagline { text-align: right; font-size: 21px; font-weight: 700; line-height: 21px; color: var(--white); }
  .tagline .accent { color: var(--cyan); }

  .hero-band { position: relative; height: 352px; background: linear-gradient(180deg, var(--steel-a), var(--steel-b)); }
  .hero { position: absolute; left: 136px; top: 0; width: 928px; height: 352px; overflow: hidden;
    background: linear-gradient(90deg, #8a8d92 0%, #9a8f8a 35%, #7c5f55 48%, #a7a9ad 62%, #6e7072 72%, #2f2f33 82%, #c9cbd2 100%); }
  .hero-title { position: absolute; left: 82px; top: 108px; color: var(--white); font-size: 72px; line-height: 66px; letter-spacing: -1px; }
  .hero-title strong { display: block; font-weight: 700; color: rgba(255,255,255,0.85); }
  .hero-title span { display: block; font-weight: 300; }
  .hero-arrow { position: absolute; top: 143px; width: 56px; height: 56px; border-radius: 50%; background: rgba(90,100,110,0.55); }
  .hero-arrow.prev { left: 108px; }
  .hero-arrow.next { left: 1036px; }
  .hero-arrow svg { position: absolute; top: 20px; }
  .hero-arrow.prev svg { left: 34px; }
  .hero-arrow.next svg { left: 14px; }

  .intro-banner { margin: 0 136px; height: 88px; background: var(--teal); color: var(--white); font-size: 19px; font-weight: 500; line-height: 27px; padding: 20px 31px; }

  .about { margin: 32px 136px 0; height: 144px; background: var(--panel); padding: 32px 32px; color: var(--body-text); font-size: 14.2px; line-height: 23px; }
  .about a { color: var(--cyan); font-weight: 700; text-decoration: none; margin-left: 4px; }

  .products { margin: 32px 136px 0; display: grid; grid-template-columns: 448px 448px; column-gap: 32px; row-gap: 32px; }
  .product-tile { position: relative; height: 192px; }
  .product-photo { position: absolute; inset: 0; }
  .product-label { position: absolute; left: 0; top: 0; height: 48px; background: var(--navy); color: var(--white); font-size: 26px; font-weight: 700; line-height: 48px; padding-left: 31px; }
  .threaded .product-photo { background: linear-gradient(135deg, #d8d6d2, #b7b5ae 55%, #8d8a7d); }
  .pins .product-photo { background: linear-gradient(135deg, #dcdcdc, #c2bfb7 50%, #5a5a5a); }
  .stampings .product-photo { background: linear-gradient(135deg, #dedfe0, #c1bfbb 60%, #9c8c7a); }
  .washers .product-photo { background: linear-gradient(135deg, #e0e1e2, #a8a397 55%, #6e7f8b); }
</style>
</head>
<body>
<div class="page">
  <nav class="main-nav">
    <a class="is-active" href="#">HOME</a>
    <a href="#">PRODUCTS</a>
    <a href="#">CAPABILITIES</a>
    <a href="#">ENGINEEERING</a>
    <a href="#">QUALITY</a>
    <a href="#">ABOUT US</a>
    <a href="#">CONTACT / QUOTE REQUEST</a>
  </nav>

  <header class="site-header">
    <div class="brand">
      <div class="brand-mark"></div>
      <div class="brand-name">KRV Holdfast Group</div>
    </div>
    <div class="tagline"><span class="accent">BETTER FASTENERS</span> FOR<br>BETTER PRODUCTS</div>
  </header>

  <section class="hero-band">
    <div class="hero" role="img" aria-label="Close-up photograph of a bolted steel flange on industrial machinery">
      <h1 class="hero-title"><strong>Revolutionizing</strong><span>the Industry</span></h1>
    </div>
    <div class="hero-arrow prev"><svg width="10" height="16" viewBox="0 0 10 16"><path d="M8 1 L2 8 L8 15" fill="none" stroke="#c9d2da" stroke-width="3"/></svg></div>
    <div class="hero-arrow next"><svg width="10" height="16" viewBox="0 0 10 16"><path d="M2 1 L8 8 L2 15" fill="none" stroke="#c9d2da" stroke-width="3"/></svg></div>
  </section>

  <div class="intro-banner">KRV Holdfast Group is a leading designer and manufacturer of value added, high quality engineered hardware solutions.</div>

  <section class="about">
    <p>Lorem ipsum dolor sit amet, consectetur adipiscing elit, sed do eiusmod tempor incididunt ut labore dolore magna aliqua ut enim ad minim veniam, quis nostrud exercitation ullamco laboris nisi ut aliquip ex ea commodo consequat. Duis aute irure dolor in reprehenderit in voluptate velit esse cillum dolore eu fugiat nulla pariatur. Excepteur sint occaecat cupidatat non proident, sunt in culpa qui officia deserunt mollit anim id est laborum. <a href="#">Find out more about us ›</a></p>
  </section>

  <section class="products">
    <article class="product-tile threaded">
      <div class="product-photo" role="img" aria-label="Photograph of assorted threaded screws and bolts"></div>
      <h2 class="product-label" style="width:200px">THREADED</h2>
    </article>
    <article class="product-tile pins">
      <div class="product-photo" role="img" aria-label="Photograph of assorted pins and clips"></div>
      <h2 class="product-label" style="width:120px">PINS</h2>
    </article>
    <article class="product-tile stampings">
      <div class="product-photo" role="img" aria-label="Photograph of assorted stamped toothed washers"></div>
      <h2 class="product-label" style="width:216px">STAMPINGS</h2>
    </article>
    <article class="product-tile washers">
      <div class="product-photo" role="img" aria-label="Photograph of assorted split lock washers"></div>
      <h2 class="product-label" style="width:264px">LOCK WASHERS</h2>
    </article>
  </section>
</div>
</body>
</html>
```